Business cards & Stationary for company
Brindlewood Asset Partners, LLC
I need double sided standard sized Business Card [3.5" x 2"]
Use whatever will work best for business cards and stationary
Professional
Marcus Tollivant
CEO & Chief Investment Officer
20431 Quill Fern Ln.
Fernhollow, QF 00417
Marcus@brindlewood-ap.example
www.brindlewood-ap.example
Behind my last name, please add the following information:
J.D., MBA, Ed.D in-progress
Feel free to utilize different styles but try to stick to the company logo colors as best as possible.
The following should be included on the back, or at least a similar version of such.
~A Different Path for Your Portfolio~TM (note - the TM is the trademark symbol
About Us:
Our firm is built on following principles:
First, consistently seek the highest possible return on client investments.
Second, help non-traditional investors who are ignored by prominent Wall Street firms.
Third, provide financial assistance to organizations, families, and veterinarians who assist abused and abandoned canines.
Company Logo for Brindlewood Asset Partners, LLC

```html
<!DOCTYPE html>
<html lang="en">
<head>
<meta charset="utf-8">
<title>Brindlewood Asset Partners – Business Card</title>
<link href="https://fonts.googleapis.com/css2?family=Cormorant+SC:wght@500;600&family=Cormorant+Garamond:wght@500;600&display=swap" rel="stylesheet">
<style>
  :root {
    --page-bg: #e9ebee;
    --card-white: #ffffff;
    --card-shade: #eef0f2;
    --brand-blue: #1f8ad8;
    --brand-sky: #36a9f0;
    --brand-navy: #1b4f7a;
    --band-grey: #5d6670;
    --text-grey: #4b535b;
  }
  * { box-sizing: border-box; margin: 0; padding: 0; }
  html, body { width: 1200px; height: 1006px; overflow: hidden; }
  body {
    background: var(--page-bg);
    font-family: "Cormorant Garamond", "Times New Roman", serif;
    color: var(--text-grey);
    display: flex;
    flex-direction: column;
    align-items: center;
    justify-content: center;
    gap: 42px;
  }
  .card {
    position: relative;
    width: 770px;
    height: 440px;
    border-radius: 26px;
    overflow: hidden;
    background: linear-gradient(160deg, var(--card-white) 40%, var(--card-shade) 100%);
    box-shadow: 0 6px 18px rgba(0,0,0,0.12);
  }

  /* Back side */
  .card-back .brand-lockup {
    position: absolute;
    top: 150px; left: 0; right: 0;
    display: flex; align-items: center; justify-content: center; gap: 18px;
  }
  .brand-square {
    width: 34px; height: 34px;
    background: var(--brand-sky);
  }
  .brand-name {
    font-family: "Cormorant SC", "Times New Roman", serif;
    font-weight: 600;
    color: var(--brand-navy);
    font-size: 46px;
    letter-spacing: 2px;
  }
  .card-back .website {
    position: absolute;
    top: 262px; left: 0; right: 0;
    text-align: center;
    font-family: "Cormorant SC", "Times New Roman", serif;
    font-size: 20px;
    letter-spacing: 6px;
    color: var(--brand-blue);
  }

  /* Front side */
  .card-front .brand-block {
    position: absolute;
    top: 46px; left: 54px;
  }
  .card-front .brand-lockup { display: flex; align-items: center; gap: 16px; }
  .card-front .brand-square { width: 30px; height: 30px; }
  .card-front .brand-name { font-size: 40px; }
  .brand-sub {
    margin-top: 2px;
    margin-left: 46px;
    font-family: "Cormorant SC", "Times New Roman", serif;
    font-weight: 600;
    font-size: 21px;
    letter-spacing: 2px;
    color: var(--brand-navy);
  }
  .tagline {
    margin-left: 46px;
    margin-top: 2px;
    font-size: 14px;
    font-style: italic;
    color: var(--text-grey);
  }
  .contact-list {
    position: absolute;
    top: 172px; left: 54px;
    list-style: none;
    font-size: 16px;
    line-height: 26px;
  }
  .contact-list li { display: flex; align-items: center; gap: 10px; }
  .contact-list svg { width: 14px; height: 14px; fill: var(--brand-blue); flex: none; }
  .person {
    position: absolute;
    right: 60px; top: 276px;
    text-align: right;
  }
  .person-name {
    font-family: "Cormorant SC", "Times New Roman", serif;
    font-weight: 600;
    font-size: 22px;
    color: var(--brand-blue);
    letter-spacing: 1px;
  }
  .person-creds { font-size: 14px; color: var(--text-grey); }
  .person-title {
    font-family: "Cormorant SC", "Times New Roman", serif;
    font-size: 15px;
    letter-spacing: 1px;
    color: var(--text-grey);
  }
  .band { position: absolute; left: 0; bottom: 0; width: 100%; height: 100px; }
  .band-website {
    position: absolute;
    right: 70px; bottom: 12px;
    font-family: "Cormorant SC", "Times New Roman", serif;
    font-size: 17px;
    line-height: 22px;
    letter-spacing: 5px;
    color: #ffffff;
  }
</style>
</head>
<body>

  <section class="card card-back" aria-label="Card back">
    <div class="brand-lockup">
      <span class="brand-square"></span>
      <span class="brand-name">Brindlewood</span>
    </div>
    <p class="website">www.brindlewood-ap.example</p>
  </section>

  <section class="card card-front" aria-label="Card front">
    <div class="brand-block">
      <div class="brand-lockup">
        <span class="brand-square"></span>
        <span class="brand-name">Brindlewood</span>
      </div>
      <p class="brand-sub">Asset Partners, LLC</p>
      <p class="tagline">~A Different Path for Your Portfolio~™</p>
    </div>

    <ul class="contact-list">
      <li><svg viewBox="0 0 24 24"><path d="M12 2a7 7 0 0 0-7 7c0 5 7 13 7 13s7-8 7-13a7 7 0 0 0-7-7zm0 9.5A2.5 2.5 0 1 1 12 6.5a2.5 2.5 0 0 1 0 5z"/></svg>20431 Quill Fern Ln.</li>
      <li><svg viewBox="0 0 24 24" style="fill:none"></svg>Fernhollow, QF 00417</li>
      <li><svg viewBox="0 0 24 24"><path d="M6.6 10.8a15 15 0 0 0 6.6 6.6l2.2-2.2a1 1 0 0 1 1-.25 11.4 11.4 0 0 0 3.6.57 1 1 0 0 1 1 1V20a1 1 0 0 1-1 1A17 17 0 0 1 3 4a1 1 0 0 1 1-1h3.5a1 1 0 0 1 1 1c0 1.250.2 2.450.57 3.57a1 1 0 0 1-.25 1z"/></svg>555-555-0148</li>
      <li><svg viewBox="0 0 24 24"><path d="M3 5h18v14H3zm2 2v.5l7 4.5 7-4.5V7l-7 4.5z"/></svg>Marcus@brindlewood-ap.example</li>
      <li><svg viewBox="0 0 24 24"><path d="M12 2a10 10 0 1 0 0 20 10 10 0 0 0 0-20zm6.9 9h-3a15 15 0 0 0-1.3-5.6A8 8 0 0 1 18.9 11zM12 4c.9 1.2 1.8 3.6 1.9 7h-3.8C10.2 7.6 11.1 5.2 12 4zM9.4 5.4A15 15 0 0 0 8.1 11h-3a8 8 0 0 1 4.3-5.6zM5.1 13h3a15 15 0 0 0 1.3 5.6A8 8 0 0 1 5.1 13zM12 20c-.9-1.2-1.8-3.6-1.9-7h3.8c-.1 3.4-1 5.8-1.9 7zm2.6-1.4a15 15 0 0 0 1.3-5.6h3a8 8 0 0 1-4.3 5.6z"/></svg>www.brindlewood-ap.example</li>
    </ul>

    <div class="person">
      <p class="person-name">Marcus Tollivant <span class="person-creds">J.D., MBA, Ed.D in-progress</span></p>
      <p class="person-title">CEO &amp; Chief Investment Officer</p>
    </div>

    <svg class="band" viewBox="0 0 770 100" preserveAspectRatio="none" aria-hidden="true">
      <path d="M0 10 H150 C190 10 200 44 240 44 H770 V100 H0 Z" fill="var(--band-grey)"/>
      <path d="M0 22 H140 C180 22 190 56 232 56 H770 V100 H0 Z" fill="var(--brand-blue)"/>
      <path d="M0 16 H145 C185 16 195 50 236 50 H770 V53 H234 C192 53 182 19 142 19 H0 Z" fill="var(--brand-sky)"/>
    </svg>
    <p class="band-website">www.brindlewood-ap.example</p>
  </section>

</body>
</html>
```